MODELS AGENCY NEW YEAR 2026 CARD

A 10 cm x 21 cm horizontal New Year card for clients of our 2 models agencies, Pommelin (kids) and Velvaride (actors and adults) (logo in the jobs).

Side A of the card: creative mission:
-text: 2026
-text: Peace and Love
-Studio or movie set atmosphere
-tone of voice: optimistic, positive, colorful

Side B:
(name of 4 people of the agency:)
Odette, Anne-Sophie, Hortense & Luc-Antoine,
(2 logos)
Pommelin & VelvaRide
(Adres)
Rue des Tilleuls 74 b3 - 1200 Bruxelles - Belgique

Target Market(s)

Movie directors, photographers

Industry/Entity Type

Fashion, advertising & Movies

Requirements
Must have
• SEE TEXT IN BRIEFING

```html
<!DOCTYPE html>
<html lang="en">
<head>
<meta charset="utf-8">
<title>New Year 2026 Card – Pommelin &amp; VelvaRide</title>
<link rel="stylesheet" href="https://fonts.googleapis.com/css2?family=Cinzel:wght@400;500&family=Montserrat:wght@300;400&family=Oswald:wght@500&display=swap">
<style>
  :root {
    --page: #e4e4e4;
    --night-top: #07090b;
    --night-bottom: #062a3d;
    --gold-line: #c9a96a;
    --gold: #e3b23c;
    --tan: #cfae7a;
    --coral: #ef6f6a;
    --sage: #86bfa6;
    --ink-light: #f4f1ea;
    --logo-ink: #3a2457;
    --white: #ffffff;
  }
  * { box-sizing: border-box; margin: 0; padding: 0; }
  html, body { width: 1200px; height: 1200px; overflow: hidden; }
  body { background: var(--page); position: relative; font-family: "Montserrat", sans-serif; }

  .card {
    position: absolute;
    left: 235px;
    width: 730px;
    height: 347px;
    background: linear-gradient(180deg, var(--night-top) 0%, #0a161d 40%, var(--night-bottom) 100%);
    overflow: hidden;
  }
  .card--front { top: 225px; }
  .card--back { top: 679px; }

  .card__rules { position: absolute; inset: 0; width: 730px; height: 347px; }

  .ornaments {
    position: absolute;
    background: linear-gradient(180deg, rgba(201,169,106,0.10) 0%, rgba(227,178,60,0.22) 60%, rgba(239,111,106,0.18) 100%);
    border-radius: 4px;
  }

  /* Front */
  .year {
    position: absolute; top: 112px; left: 0; width: 730px;
    text-align: center;
    font-family: "Oswald", sans-serif; font-weight: 500;
    font-size: 38px; letter-spacing: 0; line-height: 1;
  }
  .year .d1 { color: var(--gold); }
  .year .d2 { color: var(--tan); }
  .year .d3 { color: var(--coral); }
  .year .d4 { color: var(--sage); }

  .greeting {
    position: absolute; top: 183px; left: 265px; width: 200px;
    text-align: center;
    font-family: "Cinzel", serif; font-weight: 400;
    font-size: 25px; line-height: 30px;
    color: var(--ink-light);
    letter-spacing: 1px;
  }
  .mood {
    position: absolute; top: 220px; left: 0; width: 730px;
    text-align: center;
    font-family: "Montserrat", sans-serif; font-weight: 300;
    font-size: 14px; line-height: 18px;
    color: var(--ink-light);
    letter-spacing: 0.3px;
  }

  /* Back */
  .team {
    position: absolute; top: 155px; left: 153px; width: 420px; height: 34px;
    display: flex; align-items: center; justify-content: center; gap: 7px;
    font-family: "Cinzel", serif; font-size: 13.5px;
    color: var(--ink-light); letter-spacing: 0.4px;
  }
  .team__sep { width: 1px; height: 16px; background: var(--gold-line); }

  .agencies {
    position: absolute; top: 209px; left: 271px; width: 187px; height: 52px;
    background: var(--white);
    border-radius: 0 0 7px 7px;
    display: flex; align-items: center; justify-content: space-around;
    font-family: "Montserrat", sans-serif; font-weight: 400;
    font-size: 11px; color: var(--logo-ink); letter-spacing: 0.3px;
  }
  .address {
    position: absolute; top: 288px; left: 0; width: 730px;
    text-align: center;
    font-family: "Montserrat", sans-serif; font-weight: 300;
    font-size: 13.5px; color: var(--ink-light); letter-spacing: 0.2px;
  }
  .burst {
    position: absolute; left: 346px; top: 102px; width: 42px; height: 42px;
    border-radius: 50%;
    background: radial-gradient(circle, rgba(227,178,60,0.35) 0%, rgba(227,178,60,0) 70%);
  }
</style>
</head>
<body>

  <section class="card card--front" aria-label="Side A">
    <svg class="card__rules" viewBox="0 0 730 347" aria-hidden="true">
      <g fill="none" stroke="var(--gold-line)" stroke-width="1">
        <circle cx="365" cy="176" r="124"/>
        <circle cx="365" cy="176" r="118"/>
        <line x1="0" y1="180" x2="239" y2="180"/>
        <line x1="0" y1="184" x2="239" y2="184"/>
        <line x1="491" y1="180" x2="730" y2="180"/>
        <line x1="491" y1="184" x2="730" y2="184"/>
      </g>
      <g stroke="var(--ink-light)" stroke-width="0.8">
        <line x1="265" y1="179" x2="464" y2="179"/>
        <line x1="265" y1="216" x2="464" y2="216"/>
      </g>
    </svg>

    <div class="ornaments" style="left:19px; top:186px; width:202px; height:90px;" role="img" aria-label="Hanging gold baubles and coral stars"></div>
    <div class="ornaments" style="left:509px; top:186px; width:202px; height:90px;" role="img" aria-label="Hanging gold baubles and coral stars"></div>

    <p class="year"><span class="d1">2</span><span class="d2">0</span><span class="d3">2</span><span class="d4">6</span></p>
    <h1 class="greeting">Peace &amp; Love</h1>
    <p class="mood">Studio or movie set<br>atmosphere.</p>
  </section>

  <section class="card card--back" aria-label="Side B">
    <svg class="card__rules" viewBox="0 0 730 347" aria-hidden="true">
      <g fill="none" stroke="var(--gold-line)" stroke-width="1">
        <line x1="0" y1="168" x2="153" y2="168"/>
        <line x1="0" y1="172" x2="153" y2="172"/>
        <line x1="573" y1="168" x2="730" y2="168"/>
        <line x1="573" y1="172" x2="730" y2="172"/>
        <rect x="153" y="155" width="420" height="34" rx="6" ry="6" stroke-width="1.2"/>
      </g>
    </svg>

    <div class="burst" role="img" aria-label="Small golden firework"></div>

    <div class="ornaments" style="left:16px; top:174px; width:129px; height:59px;" role="img" aria-label="Hanging gold baubles and coral stars"></div>
    <div class="ornaments" style="left:589px; top:174px; width:130px; height:59px;" role="img" aria-label="Hanging gold baubles and coral stars"></div>

    <p class="team">
      <span>Odette</span><span class="team__sep"></span>
      <span>Anne-Sophie</span><span class="team__sep"></span>
      <span>Hortense</span><span class="team__sep"></span>
      <span>Luc-Antoine</span>
    </p>

    <div class="agencies">
      <span class="agencies__name">Pommelin</span>
      <span class="agencies__name">VelvaRide</span>
    </div>

    <p class="address">Rue des Tilleuls 74 b3 - 1200 Bruxelles - Belgique</p>
  </section>

</body>
</html>
```